FLYER für Fortbildung
Zielgruppe
Die Fortbildung, die beworben werden soll, richtet sich an Fachkräfte, die in Kitas arbeiten. In diesem Fall handelt es sich um eine praxisorientierte Online-Live-Fortbildung - dies bedeutet, die TeilnehmerInnen werden während der Online-Fortbildung kontinuierlich durch eine Referentin begleitet. Die Fortbildung erweitert das Wissen und die Kompetenzen der Teilnehmenden.
Aufgabenstellung
Ich freue mich über Vorschläge eines Falzflyers im Format DIN lang. Wie viele Seiten der Flyer umfasst, überlasse ich gerne Ihnen, da dies von Ihrer Gestaltung abhängt.
Falls Sie 1-4 Bilder einfügen möchten, gebe ich Ihnen in den Datei-Upload gerne einige Beispiele, die mir zusagen (zur Auswahl). Darüber hinaus bin ich selbstverständlich auch offen für alternative Vorschläge sowie neue Designs.

```html
<!DOCTYPE html>
<html lang="de">
<head>
<meta charset="utf-8">
<title>Falzflyer – Neue Horizonte für Kita-Fachkräfte</title>
<link href="https://fonts.googleapis.com/css2?family=Montserrat:wght@500;600;700&family=Open+Sans:wght@400;600;700&display=swap" rel="stylesheet">
<style>
  :root {
    --bg: #eeeeee;
    --paper: #ffffff;
    --sage: #e3ebdb;
    --panel-grey: #eceef1;
    --panel-soft: #f4f4f5;
    --navy: #4b5f7e;
    --text: #4a4f57;
    --gold: #b08b4c;
    --photo-a: #d9c9b4;
    --photo-b: #8fa0b3;
  }
  * { box-sizing: border-box; margin: 0; padding: 0; }
  html, body { width: 1200px; height: 686px; overflow: hidden; }
  body {
    background: var(--bg);
    font-family: "Open Sans", Arial, sans-serif;
    color: var(--text);
    position: relative;
  }
  .flyer {
    position: absolute; left: 50px; top: 120px;
    width: 1100px; height: 446px;
    display: flex;
    box-shadow: 0 14px 30px rgba(0,0,0,.12);
  }
  .panel { width: 220px; height: 100%; position: relative; padding: 34px 20px; }
  .panel + .panel { border-left: 1px solid #e2e2e2; }
  .panel--contact { background: var(--sage); text-align: center; }
  .panel--benefits { background: var(--paper); }
  .panel--modules { background: var(--panel-grey); }
  .panel--voices { background: var(--panel-soft); }
  .panel--cover { background: var(--paper); padding: 24px 0 0; text-align: center; }

  .brand { display: flex; flex-direction: column; align-items: center; gap: 6px; }
  .brand__dot { width: 34px; height: 34px; border-radius: 50%; background: var(--gold); opacity: .85; }
  .brand__name {
    font-family: "Montserrat", Arial, sans-serif; font-weight: 600;
    font-size: 16px; letter-spacing: .5px; color: var(--navy); line-height: 1.15;
  }
  .brand__tag { font-family: "Montserrat", Arial, sans-serif; font-weight: 600; font-size: 8.5px; letter-spacing: 2px; color: var(--navy); }

  .contact__blurb { font-size: 9.5px; line-height: 1.45; margin: 16px 0 34px; text-align: left; }
  .contact__list { list-style: none; font-size: 9.5px; line-height: 1.6; margin-top: 60px; text-align: left; padding-left: 10px; }

  h2 { font-family: "Montserrat", Arial, sans-serif; font-weight: 600; color: var(--navy); font-size: 15px; margin-bottom: 10px; }
  .intro { font-size: 9.5px; line-height: 1.45; margin-bottom: 28px; }
  .benefits { list-style: none; font-size: 9.5px; line-height: 1.4; }
  .benefits li { display: flex; gap: 6px; margin-bottom: 6px; align-items: flex-start; }
  .benefits svg { flex: 0 0 10px; margin-top: 3px; }

  .module-block { margin-bottom: 60px; }
  .module-grid { display: grid; grid-template-columns: 1fr 1fr; gap: 8px; font-size: 9px; line-height: 1.45; }
  .module-grid strong { display: block; color: var(--navy); font-weight: 700; }

  .panel--voices h2 { margin: 90px 0 14px; font-size: 13px; }
  .quote { border: 1px solid var(--gold); padding: 14px 14px 12px; margin-bottom: 18px; position: relative; font-size: 9px; line-height: 1.45; background: var(--paper); }
  .quote::before, .quote::after { font-family: Georgia, serif; color: var(--gold); font-size: 22px; position: absolute; line-height: 1; }
  .quote::before { content: "\201C"; left: 4px; top: -8px; background: var(--panel-soft); padding: 0 2px; }
  .quote::after { content: "\201D"; right: 4px; bottom: -12px; background: var(--panel-soft); padding: 0 2px; }
  .quote cite { display: block; text-align: right; font-style: normal; margin-top: 6px; }
  .voices__note { position: absolute; bottom: 20px; left: 0; right: 0; text-align: center; font-size: 7.5px; }

  .cover__photo { height: 150px; margin: 16px 0 0; background: linear-gradient(135deg, var(--photo-a), var(--photo-b)); }
  .cover__title { font-family: "Montserrat", Arial, sans-serif; font-weight: 600; color: var(--navy); font-size: 19px; line-height: 1.2; margin: 22px 16px 10px; }
  .cover__rule { height: 1px; background: var(--gold); margin: 0 24px 14px; }
  .cover__cta { display: inline-block; background: var(--gold); color: #fff; font-size: 9.5px; font-weight: 600; padding: 6px 14px; border-radius: 14px; }
</style>
</head>
<body>
<main class="flyer">
  <section class="panel panel--contact">
    <div class="brand">
      <span class="brand__dot"></span>
      <span class="brand__name">KLARER ARBEITSTAG</span>
      <span class="brand__tag">COACHING &amp; SUPERVISION</span>
    </div>
    <p class="contact__blurb">Unsere praxisorientierte Online-Live-Fortbildung begleitet Sie kontinuierlich mit Referentin – bequem von zu Hause.</p>
    <div class="brand">
      <span class="brand__dot"></span>
      <span class="brand__name">KLARER ARBEITSTAG</span>
      <span class="brand__tag">COACHING &amp; SUPERVISION</span>
    </div>
    <ul class="contact__list">
      <li>Web: www.klarer-arbeitstag.de</li>
      <li>Email: info@klarer-arbeitstag.de</li>
      <li>Tel.: 0123-907415</li>
    </ul>
  </section>

  <section class="panel panel--benefits">
    <h2>Stärker im Kita-Alltag</h2>
    <p class="intro">Unsere praxisorientierte Online-Fortbildung bietet speziell für Fachkräfte in Kitas neue Impulse, fundiertes Wissen und direkte Begleitung durch eine Referentin.</p>
    <h2>Ihre Vorteile</h2>
    <ul class="benefits">
      <li><svg width="10" height="10" viewBox="0 0 10 10"><circle cx="5" cy="5" r="4" fill="none" stroke="#b08b4c"/></svg>Fundiertes Wissen für den Alltag</li>
      <li><svg width="10" height="10" viewBox="0 0 10 10"><circle cx="5" cy="5" r="4" fill="none" stroke="#b08b4c"/></svg>Praxisnahe Methoden sofort anwendbar</li>
      <li><svg width="10" height="10" viewBox="0 0 10 10"><circle cx="5" cy="5" r="4" fill="none" stroke="#b08b4c"/></svg>Live begleitet durch eine Referentin</li>
      <li><svg width="10" height="10" viewBox="0 0 10 10"><circle cx="5" cy="5" r="4" fill="none" stroke="#b08b4c"/></svg>Sicherer im Berufsalltag agieren</li>
      <li><svg width="10" height="10" viewBox="0 0 10 10"><circle cx="5" cy="5" r="4" fill="none" stroke="#b08b4c"/></svg>Direkter Austausch</li>
      <li><svg width="10" height="10" viewBox="0 0 10 10"><circle cx="5" cy="5" r="4" fill="none" stroke="#b08b4c"/></svg>Inspirierendes Netzwerk knüpfen</li>
      <li><svg width="10" height="10" viewBox="0 0 10 10"><circle cx="5" cy="5" r="4" fill="none" stroke="#b08b4c"/></svg>Mehr Zufriedenheit im Job erleben</li>
    </ul>
  </section>

  <section class="panel panel--modules">
    <div class="module-block">
      <h2>Modulübersicht</h2>
      <div class="module-grid">
        <div><strong>Modul 1</strong>Kommunikation im Team<br>2. Elterngespräche<br>3. Resilienz stärken</div>
        <div><strong>Modul 4</strong>5. Konfliktlösung<br>Teamentwicklung</div>
      </div>
    </div>
    <div class="module-block">
      <h2>Modulinhalte</h2>
      <div class="module-grid">
        <div><strong>Modul 1</strong>Umgang im Team<br>2. Konfliktklärung<br>3. Kommunikation</div>
        <div><strong>Modul 4</strong>Achtsamkeit<br>5. Arbeitsorganisation<br>6. Selbstfürsorge</div>
      </div>
    </div>
  </section>

  <section class="panel panel--voices">
    <h2>Das sagen Teilnehmende</h2>
    <blockquote class="quote">Die Fortbildung hat mir neue Impulse gegeben. Ich fühle mich gestärkt!<cite>– Jana T.</cite></blockquote>
    <blockquote class="quote">Die Fortbildung hat meinen Berufsalltag erweitert. Die Referentin war fantastisch!<cite>– Timo R.</cite></blockquote>
    <p class="voices__note">Details &amp; Termine auf unserer Website</p>
  </section>

  <section class="panel panel--cover">
    <div class="brand">
      <span class="brand__dot"></span>
      <span class="brand__name">KLARER ARBEITSTAG</span>
      <span class="brand__tag">COACHING &amp; SUPERVISION</span>
    </div>
    <div class="cover__photo" role="img" aria-label="Foto: Gruppe von Kita-Fachkräften im Gespräch an einem hellen Tisch"></div>
    <h1 class="cover__title">Neue Horizonte<br>für Kita-Fachkräfte</h1>
    <div class="cover__rule"></div>
    <span class="cover__cta">Jetzt informieren &amp; anmelden!</span>
  </section>
</main>
</body>
</html>
```